We are a doctors medical practice
I need the business card to be eye catching and memorable,
to reflect professionalism, yet also warmth and care

the numbers need to be easy to see, for the elderly

and the logo also in a location that is large enough to see and be eye catching

Back of card:
opening hours:
Mon- Fri 8.30am to 6pm
Sat 9am to 4pm

rows for appontments, date and time
Updates

HiĀ 

Modification to company name

BROOKVALE KINDRED HEALTH MEDICAL PRACTICE

Thanks
Marla

Reason: I am look for a unique design that also fulfils the design brief

I have attempted to post a .eps and .ai file of the logo

Target Market(s)

needs to appeal to the majority, mainly adults

Industry/Entity Type

Medical

Contact Information for Business Card

company name: Brookvale Kindred Health Medical Practice
Name: Dr Marla Vossberg-Tait
Qualifications: MBBS, Bsci(med), FRACGP, DCH, SH&FPA, Dip Derm
Address: Shop 3/41-43 Quorrow St, Brookvale 2940
Ph: 02 9418 3052
Fax: 02 9461 8824

Requirements
Nice to have
• I like balance
gold/ silver incorporated, as well as the other colours in the logo- but not limited to these colours
a "medical" feel
Should not have
• dark or strong colours

```html
<!DOCTYPE html>
<html lang="en">
<head>
<meta charset="utf-8">
<title>Brookvale Kindred Health Medical Practice – Business Card</title>
<link rel="stylesheet" href="https://fonts.googleapis.com/css2?family=Montserrat:wght@600&family=Roboto+Condensed:ital,wght@0,400;0,700;1,400&display=swap">
<style>
  :root {
    --page-bg: #eef2ec;
    --card-bg: #ffffff;
    --brand-blue: #1aa3e0;
    --brand-green: #7ab83a;
    --ink-grey: #c9c9c9;
    --rule-grey: #bdbdbd;
    --card-shadow: 0 10px 24px rgba(40, 60, 40, 0.22);
  }
  * { box-sizing: border-box; margin: 0; padding: 0; }
  html, body {
    width: 1200px;
    height: 900px;
    overflow: hidden;
    background: var(--page-bg);
  }
  .canvas {
    position: relative;
    width: 1200px;
    height: 900px;
  }
  .card {
    position: absolute;
    left: 290px;
    width: 620px;
    height: 354px;
    background: var(--card-bg);
    box-shadow: var(--card-shadow);
  }
  .card--front { top: 70px; }
  .card--back  { top: 476px; }

  /* Front */
  .brand {
    position: absolute;
    left: 130px;
    top: 118px;
    display: flex;
    align-items: center;
    gap: 26px;
  }
  .brand__dot {
    width: 110px;
    height: 110px;
    border-radius: 50%;
    background: var(--brand-green);
    flex: none;
  }
  .brand__name {
    font-family: "Montserrat", sans-serif;
    font-weight: 600;
    color: var(--brand-blue);
    font-size: 25px;
    line-height: 1.05;
    letter-spacing: 0.01em;
  }

  /* Back */
  .appointments {
    position: absolute;
    left: 40px;
    top: 62px;
    width: 258px;
  }
  .appointments__row {
    height: 38px;
    border-bottom: 1px dashed var(--rule-grey);
  }
  .hours {
    position: absolute;
    left: 40px;
    top: 272px;
    width: 258px;
    text-align: center;
    font-family: "Roboto Condensed", sans-serif;
    color: var(--ink-grey);
    font-size: 13px;
    line-height: 1.4;
  }
  .hours__label { font-style: italic; }

  .doctor {
    position: absolute;
    left: 330px;
    top: 50px;
    font-family: "Roboto Condensed", sans-serif;
    color: var(--brand-blue);
  }
  .doctor__name {
    font-size: 23px;
    font-weight: 700;
    letter-spacing: 0.01em;
  }
  .doctor__quals {
    font-size: 9.5px;
    margin-top: 3px;
  }
  .address {
    margin-top: 34px;
    margin-left: 10px;
    font-size: 18px;
    line-height: 1.3;
  }
  .contact {
    margin-top: 26px;
    margin-left: 14px;
    font-size: 18px;
    line-height: 1.35;
  }
  .contact__phone { font-weight: 700; }
</style>
</head>
<body>
<main class="canvas">

  <section class="card card--front" aria-label="Business card front">
    <div class="brand">
      <span class="brand__dot" aria-hidden="true"></span>
      <h1 class="brand__name">BROOKVALE<br>KINDRED HEALTH<br>MEDICAL PRACTICE</h1>
    </div>
  </section>

  <section class="card card--back" aria-label="Business card back">
    <div class="appointments" aria-label="Appointment rows">
      <div class="appointments__row"></div>
      <div class="appointments__row"></div>
      <div class="appointments__row"></div>
      <div class="appointments__row"></div>
      <div class="appointments__row"></div>
    </div>
    <p class="hours">
      <span class="hours__label">opening hours:</span><br>
      Mon- Fri 8.30am to 6pm - Sat 9am to 4pm
    </p>

    <div class="doctor">
      <h2 class="doctor__name">Dr Marla Vossberg-Tait</h2>
      <p class="doctor__quals">MBBS, Bsci(med), FRACGP, DCH, SH&amp;FPA, Dip Derm</p>
      <address class="address" style="font-style:normal">
        Shop 3<br>41-43 Quorrow St<br>Brookvale 2940
      </address>
      <p class="contact">
        <span class="contact__phone">Ph: 02 9418 3052</span><br>
        Fax: 02 9461 8824
      </p>
    </div>
  </section>

</main>
</body>
</html>
```